Info flyer to showcase security vantagecam install and remote video monitoring.

I am looking for an attractive looking flyer that is simple and has some text content and some photos to show prospective clients what services I can provide them.

The two main services that I want to showcase are:
1. Security vantagecam & NVR Installations and maintenance
2. Remote Video Monitoring for business. This can be a temporary service or ongoing/long term.

Target Market(s)

Construction, Retail, Industrial, Commercial

Industry/Entity Type

Security

Font styles to use
Serif

Colors

Designer to choose colors to be used in the design.

```html
<!DOCTYPE html>
<html lang="en">
<head>
<meta charset="utf-8">
<title>Vantage Secure Systems – Security Camera Flyer</title>
<link rel="stylesheet" href="https://fonts.googleapis.com/css2?family=Nunito:wght@700;800;900&display=swap">
<style>
  :root {
    --stage: #2b2b2d;
    --paper: #ffffff;
    --gold: #d6a42b;
    --charcoal: #3a3a3c;
    --ink: #2f2f31;
    --photo-light: #cfd6de;
    --photo-mid: #8d9aab;
  }
  * { box-sizing: border-box; margin: 0; padding: 0; }
  html, body { width: 1200px; height: 822px; overflow: hidden; background: var(--stage); }
  .canvas { position: relative; width: 1200px; height: 822px; }
  .flyer {
    position: absolute; left: 330px; top: 29px;
    width: 540px; height: 764px; overflow: hidden;
    background: var(--paper);
    font-family: "Nunito", sans-serif;
  }
  .hero-photo {
    position: absolute; left: 0; top: 0; width: 540px; height: 480px;
    background: linear-gradient(135deg, var(--photo-light) 0%, var(--photo-mid) 55%, #a9b5c3 100%);
  }
  .shapes { position: absolute; inset: 0; width: 540px; height: 764px; }
  .brand {
    position: absolute; right: 22px; top: 24px;
    background: var(--paper); border-radius: 6px;
    padding: 10px 18px; display: flex; align-items: center; gap: 10px;
    font-weight: 900; font-size: 22px; color: var(--charcoal);
  }
  .brand-dot { width: 22px; height: 22px; border-radius: 50%; background: var(--gold); }
  .camera-photo {
    position: absolute; right: 22px; top: 260px; width: 190px; height: 120px;
    background: linear-gradient(135deg, #e7e9ec, #9aa1aa);
    border-radius: 4px;
  }
  .headline {
    position: absolute; left: 36px; top: 424px;
    font-weight: 900; font-size: 33px; line-height: 1.08; color: var(--gold);
  }
  .service-note {
    position: absolute; left: 36px; top: 548px; width: 260px;
    font-weight: 800; font-size: 15px; line-height: 1.35; color: var(--ink);
  }
  .contact {
    position: absolute; right: 20px; top: 664px; text-align: right; color: var(--paper);
  }
  .contact-phone { font-weight: 900; font-size: 26px; color: var(--gold); line-height: 1.15; }
  .contact-line { font-weight: 700; font-size: 14px; line-height: 1.35; }
  .social { display: flex; justify-content: flex-end; align-items: center; gap: 4px; margin-top: 3px; font-weight: 700; font-size: 14px; }
  .social-box { width: 14px; height: 14px; background: var(--gold); border-radius: 2px; }
  .social-handle { margin-left: 4px; }
</style>
</head>
<body>
<main class="canvas">
  <article class="flyer">
    <div class="hero-photo" role="img" aria-label="Photo of ceiling-mounted dome security cameras in a bright commercial building"></div>

    <svg class="shapes" viewBox="0 0 540 764" aria-hidden="true">
      <path d="M0,362 C190,352 380,260 540,120 L540,160 C390,290 200,390 0,400 Z" fill="var(--charcoal)"/>
      <path d="M0,385 C200,372 400,282 540,155 L540,182 C400,302 200,392 0,402 Z" fill="var(--gold)"/>
      <path d="M0,400 C200,390 400,300 540,180 L540,764 L0,764 Z" fill="var(--paper)"/>
      <path d="M0,742 C200,708 420,588 540,332 L540,360 C420,610 200,730 0,764 Z" fill="var(--gold)"/>
      <path d="M0,764 C200,730 420,610 540,360 L540,764 Z" fill="var(--charcoal)"/>
    </svg>

    <div class="brand"><span class="brand-dot"></span>Vantage Secure Systems</div>

    <div class="camera-photo" role="img" aria-label="Photo of a dome camera and bullet camera mounted on a bracket"></div>

    <h1 class="headline">Security Camera<br>&amp; NVR Installations<br>and maintenance</h1>

    <p class="service-note">Remote Video Monitoring for business. This can be a temporary service or ongoing/long term.</p>

    <div class="contact">
      <p class="contact-phone">PH: 555-0142-370</p>
      <p class="contact-line">hello@vantagesecure.net</p>
      <p class="contact-line">www.vantagesecure.net</p>
      <div class="social">
        <span class="social-box"></span><span class="social-box"></span><span class="social-box"></span>
        <span class="social-handle">vantagecam</span>
      </div>
    </div>
  </article>
</main>
</body>
</html>
```